Yacht, Boats, Watersports company needs a redesign of business card

Hello Designers!
We are a Boat dealership company that sells fun in the water, we sell boats, Yachts, Kayaks and also yacht WaterSport toys. We are looking to redesign our business cards in to something a little bit more sophisticated. in a way that we can make better use of our company colors. I'm attaching a zipped file containing the company 3 sets of company logo which one is an horizontal another one is a vertical and also a chromed 3d logo. Also is included two set of business cards that we use and also some designs that i think it's interesting. We use PMS 2026c Orange and PMS 7687C Blue. I would like to see at least two different options with the orange as accent and also using blue as an accent color. It's really important for the business cards to have a font option and size that is legible to most people. Our current website is wwww.corvellamarine.com. Please visit if you want to have a better feeling of the Boat dealership
You can send Single sided or double side options. We are now using single sided but we may be open for a double side option if we really like the design.
Target Market(s)
Marine, boat sales, yacht sales, water toys sales/
Contact Information for Business Card
Name: Dale Pritchett
Address: 718 West Halden Lane,
Dania Beach, FL 33019
Phone: 954-382-7146
Fax: 954:382-7139
Cell: 954-451-8320
Email: 212@corvellamarine.com
Website: corvellamarine.com
Requirements
Must have
- the current information of the business card provided.
logo
use the PMS Colors
Nice to have
- a touch of elegance and sophistication but simple
Should not have
- should not have any typography that is hard to read, the card should be simple but yet sophisticated.

```html
<!DOCTYPE html>
<html lang="en">
<head>
<meta charset="utf-8">
<title>Corvella Marine — Business Card</title>
<link rel="stylesheet" href="https://fonts.googleapis.com/css2?family=Montserrat:wght@400;500;600;700&display=swap">
<style>
  :root {
    --navy: #1e4289;
    --orange: #f4643a;
    --white: #ffffff;
    --page: #ffffff;
    --shadow: rgba(0, 0, 0, 0.28);
  }
  * { margin: 0; padding: 0; box-sizing: border-box; }
  html, body {
    width: 996px;
    height: 1200px;
    overflow: hidden;
    background: var(--page);
  }
  .canvas {
    position: relative;
    width: 996px;
    height: 1200px;
    font-family: "Montserrat", sans-serif;
  }
  .card {
    position: absolute;
    left: 179px;
    width: 660px;
    height: 377px;
    overflow: hidden;
    box-shadow: 10px 14px 22px var(--shadow);
  }
  .card-front { top: 153px; background: var(--navy); }
  .card-back  { top: 651px; background: var(--orange); }
  .card-stripes {
    position: absolute;
    left: 0;
    top: 0;
    width: 660px;
    height: 377px;
  }
  .brand-name {
    position: absolute;
    left: 474px;
    top: 188px;
    transform: translate(-50%, -50%);
    color: var(--white);
    font-weight: 700;
    font-size: 30px;
    letter-spacing: 0.5px;
    white-space: nowrap;
  }
  .website {
    position: absolute;
    left: 354px;
    top: 328px;
    color: var(--white);
    font-weight: 600;
    font-size: 16px;
    letter-spacing: 0.3px;
  }
  .contact {
    position: absolute;
    left: 316px;
    top: 0;
    color: var(--white);
  }
  .person-name {
    position: absolute;
    top: 66px;
    left: 0;
    font-size: 28px;
    color: var(--navy);
    font-weight: 500;
    white-space: nowrap;
    letter-spacing: 0.3px;
  }
  .person-name strong { font-weight: 700; }
  .person-role {
    position: absolute;
    top: 104px;
    left: 0;
    font-size: 12px;
    font-weight: 700;
    white-space: nowrap;
  }
  .role-rule {
    position: absolute;
    top: 130px;
    left: 0;
    width: 195px;
    height: 2px;
    background: var(--white);
  }
  .role-rule::before {
    content: "";
    position: absolute;
    left: 0;
    top: -1.5px;
    width: 34px;
    height: 5px;
    background: var(--white);
  }
  .contact-line {
    position: absolute;
    left: 0;
    font-size: 15px;
    font-weight: 600;
    white-space: nowrap;
    letter-spacing: 0.4px;
  }
  .address-1 { top: 166px; }
  .address-2 { top: 186px; }
  .phone     { top: 216px; }
  .fax       { top: 241px; }
  .cell      { top: 266px; }
  .email     { top: 297px; }
</style>
</head>
<body>
<main class="canvas">

  <section class="card card-front" aria-label="Card front">
    <svg class="card-stripes" viewBox="0 0 440 251" preserveAspectRatio="none" aria-hidden="true">
      <g fill="var(--orange)">
        <polygon points="0,0 57,0 174,188 90,188 0,43"/>
        <polygon points="0,62 78,188 66,188 0,82"/>
        <polygon points="62,0 73,0 140,90 129,90"/>
        <polygon points="80,0 92,0 159,90 147,90"/>
      </g>
    </svg>
    <div class="brand-name">Corvella Marine</div>
    <p class="website">www.corvellamarine.com</p>
  </section>

  <section class="card card-back" aria-label="Card back">
    <svg class="card-stripes" viewBox="0 0 440 251" preserveAspectRatio="none" aria-hidden="true">
      <g fill="var(--white)">
        <polygon points="0,0 48,0 187,211 113,211 0,40"/>
        <polygon points="0,58 58,146 46,146 0,76"/>
        <polygon points="56,0 67,0 114,71 103,71"/>
        <polygon points="75,0 87,0 128,62 116,62"/>
      </g>
    </svg>
    <div class="contact">
      <h1 class="person-name"><strong>DALE</strong> PRITCHETT</h1>
      <p class="person-role">Co-Founder Brand Name</p>
      <div class="role-rule"></div>
      <p class="contact-line address-1">718 West Halden Lane,</p>
      <p class="contact-line address-2">Dania Beach, FL 33019</p>
      <p class="contact-line phone">P: 954-382-7146</p>
      <p class="contact-line fax">F: 954-382-7139</p>
      <p class="contact-line cell">C: 954-451-8320</p>
      <p class="contact-line email">212@corvellamarine.com</p>
    </div>
  </section>

</main>
</body>
</html>
```